Business Card Design needed for logo design project

Our business needs a business card design. I'm not sure what format files are generally delivered back, but clearly I will need the ability to edit to add colleagues contact details.

Our logo is attached.

Brivanor is a 3D design services company, providing app, serious/educational game, VR and AR websites/applications to corporate clients.

Target Market(s)

Corporate blue-chip clients needing 3D design services

Industry/Entity Type

Business

Font styles to use
Sans Serif

Requirements
Must have
• Templated such that I can add details (name, phone number etc). Needs to include logo from previous project winner - attached.

```html
<!DOCTYPE html>
<html lang="en">
<head>
<meta charset="utf-8">
<title>Brivanor Business Card</title>
<link href="https://fonts.googleapis.com/css2?family=Mulish:wght@400;800&display=swap" rel="stylesheet">
<style>
  :root {
    --bg: #e6e4e1;
    --brand-red: #e31e26;
    --deep-red: #b72025;
    --ink: #3b3b3b;
    --paper: #ffffff;
  }
  html, body {
    margin: 0;
    padding: 0;
    width: 1200px;
    height: 1000px;
    overflow: hidden;
    background: var(--bg);
    font-family: "Mulish", sans-serif;
  }
  .canvas { position: relative; width: 1200px; height: 1000px; }
  .card {
    position: absolute;
    left: 265px;
    width: 667px;
    height: 397px;
    overflow: hidden;
    box-shadow: 0 6px 14px rgba(0,0,0,0.25);
  }
  .card-front { top: 73px; background: var(--deep-red); }
  .card-back { top: 533px; background: var(--paper); }

  .deco-circle {
    position: absolute;
    border-radius: 50%;
    background: var(--brand-red);
  }
  .card-front .deco-circle { left: -5px; top: 27px; width: 340px; height: 340px; }
  .card-back .deco-circle { left: 340px; top: 3px; width: 370px; height: 370px; }

  .brand {
    position: absolute;
    display: flex;
    align-items: center;
    gap: 10px;
    font-weight: 400;
    letter-spacing: 1px;
  }
  .brand-dot { border-radius: 50%; flex: none; }
  .card-front .brand { left: 320px; top: 298px; color: var(--paper); font-size: 42px; }
  .card-front .brand-dot { width: 64px; height: 64px; border: 3px solid var(--paper); box-sizing: border-box; }
  .card-back .brand { left: 33px; top: 32px; color: var(--ink); font-size: 44px; }
  .card-back .brand-dot { width: 66px; height: 66px; background: var(--brand-red); }

  .person { position: absolute; left: 33px; top: 142px; }
  .person-name { margin: 0; color: var(--brand-red); font-weight: 800; font-size: 22px; letter-spacing: 0.5px; }
  .person-role { margin: 2px 0 0; color: var(--ink); font-size: 16px; }

  .contacts { position: absolute; left: 33px; top: 208px; margin: 0; padding: 0; list-style: none; color: var(--ink); font-size: 16px; }
  .contacts li { display: flex; align-items: center; height: 24.5px; }
  .contacts li.gap { margin-top: 6px; }
  .contacts svg { width: 14px; height: 14px; margin-right: 10px; fill: var(--brand-red); flex: none; }
</style>
</head>
<body>
<div class="canvas">
  <section class="card card-front">
    <div class="deco-circle"></div>
    <div class="brand"><span class="brand-dot"></span><span class="brand-name">BRIVANOR</span></div>
  </section>

  <section class="card card-back">
    <div class="deco-circle"></div>
    <div class="brand"><span class="brand-dot"></span><span class="brand-name">BRIVANOR</span></div>
    <div class="person">
      <h1 class="person-name">ELIAS TARROWBY</h1>
      <p class="person-role">Executive Director</p>
    </div>
    <ul class="contacts">
      <li><svg viewBox="0 0 14 14"><path d="M4 0h6a1 1 0 0 1 1 1v12a1 1 0 0 1-1 1H4a1 1 0 0 1-1-1V1a1 1 0 0 1 1-1zm0.5 1.5v10h5v-10z"/></svg>+61 400 218 365</li>
      <li><svg viewBox="0 0 14 14"><path d="M1 4c0-2 3-3 6-3s6 1 6 3v1h-3V3.5H4V5H1zM3 6h8l2 6H1z"/></svg>+61 3 8012 4470</li>
      <li><svg viewBox="0 0 14 14"><path d="M3 0h8v4H3zM0 5h14v6h-2V9H2v2H0zM3 10h8v4H3z"/></svg>+61 3 8012 4471</li>
      <li class="gap"><svg viewBox="0 0 14 14"><path d="M0 3h14v1L7 8 0 4zM0 5.5l7 4 7-4V11H0z"/></svg>elias@brivanor.com</li>
      <li><svg viewBox="0 0 14 14"><path d="M7 0a7 7 0 1 0 0 14A7 7 0 0 0 7 0zm0 1.5c1 1 1.6 2.6 1.8 4.5H5.2C5.4 4.1 6 2.5 7 1.5zM1.6 6h2.2c.1-1.7.6-3.1 1.2-4.1A5.5 5.5 0 0 0 1.6 6zm8.6 0h2.2A5.5 5.5 0 0 0 9 1.9c.6 1 1.1 2.4 1.2 4.1zM1.6 8A5.5 5.5 0 0 0 5 12.1C4.4 11.1 3.9 9.7 3.8 8zm3.6 0c.2 1.9.8 3.5 1.8 4.5 1-1 1.6-2.6 1.8-4.5zm5 0c-.1 1.7-.6 3.1-1.2 4.1A5.5 5.5 0 0 0 12.4 8z"/></svg>www.brivanor.com</li>
      <li class="gap"><svg viewBox="0 0 14 14"><path d="M7 0a4.5 4.5 0 0 0-4.5 4.5C2.5 8 7 14 7 14s4.5-6 4.5-9.5A4.5 4.5 0 0 0 7 0zm0 6.3a1.8 1.8 0 1 1 0-3.6 1.8 1.8 0 0 1 0 3.6z"/></svg>14 Callister Road Epping VIC 3076</li>
    </ul>
  </section>
</div>
</body>
</html>
```